App Design for quiz app (casual gaming app)

We need an design & logo for our quiz app. Its a simple quiz app, where you pick up a category, answer three questions out of this category. After this an opponent is assigned to your game, and has to answer the same three questions. After this first round is finished, it's the opponents turn to choose a new category and answer three questions out of this category. Now it's your turn to answer the same three questions. With this done, the 2nd round is finished. One game has seven rounds.
Please find attached the balsamiq project. For all of you, do not have balsamiq, please find also the mockups as pdf.
Final delivery should be psd files
Target Market(s)
Casual Games

```html
<!DOCTYPE html>
<html lang="en">
<head>
<meta charset="utf-8">
<title>Hexa Quiz – Game Screens</title>
<link rel="stylesheet" href="https://fonts.googleapis.com/css2?family=Fredoka:wght@400;500;600;700&display=swap">
<style>
  :root {
    --page-bg: #1f1f20;
    --purple-deep: #3a0d6e;
    --purple-mid: #5a1494;
    --purple-bright: #6e16a3;
    --row-band: #3d2a8c;
    --row-edge: #7a3cf0;
    --panel: #6a1a8f;
    --panel-line: #4c0f72;
    --magenta: #a81c8c;
    --magenta-dark: #4a0c4e;
    --teal: #3ad8b4;
    --teal-soft: #56e3c2;
    --lilac: #c9a6ee;
    --white: #ffffff;
    --green-label: #2fe35a;
    --green-btn: #20cf86;
    --green-dark: #0e3a2a;
    --score-bg: #1fbf82;
    --red-dot: #ea4a4a;
    --green-dot: #12b97d;
    --avatar-fill: #5be0e8;
  }
  * { margin: 0; padding: 0; box-sizing: border-box; }
  html, body { width: 1200px; height: 1143px; overflow: hidden; background: var(--page-bg); }
  body { position: relative; font-family: "Fredoka", sans-serif; }

  .screen {
    position: absolute; top: 67px; width: 572px; height: 1008px; overflow: hidden;
    background: linear-gradient(160deg, var(--purple-mid) 0%, var(--purple-bright) 30%, var(--purple-deep) 100%);
  }
  .screen--games { left: 20px; }
  .screen--match { left: 608px; }
  .abs { position: absolute; }

  .avatar { position: absolute; }
  .avatar svg { width: 100%; height: 100%; display: block; }

  /* Games list */
  .username { left: 211px; top: 112px; font-size: 46px; font-weight: 600; color: var(--white); transform: rotate(-3deg); white-space: nowrap; }
  .header-band { left: 0; top: 200px; width: 572px; height: 120px; background: rgba(40, 10, 80, 0.35); transform: skewY(-4deg); }
  .create-btn {
    left: 96px; top: 250px; width: 382px; height: 70px; background: var(--magenta);
    color: var(--magenta-dark); font-size: 38px; font-weight: 600; display: flex; align-items: center; justify-content: center;
    transform: rotate(-4deg); box-shadow: 0 6px 0 #6c1060; white-space: nowrap;
  }
  .section-label { font-size: 32px; font-weight: 600; color: var(--teal-soft); transform: rotate(-3deg); white-space: nowrap; }
  .section-label--done { color: var(--green-label); }
  .game-row {
    left: 0; width: 572px; height: 118px;
    background: linear-gradient(90deg, var(--row-band), rgba(90, 60, 170, 0.9));
    border-bottom: 4px solid var(--row-edge); transform: skewY(-4deg); transform-origin: left;
  }
  .round-info { width: 120px; text-align: center; color: var(--teal); transform: rotate(-3deg); white-space: nowrap; }
  .round-info .round { font-size: 29px; font-weight: 400; display: block; }
  .round-info .score { font-size: 40px; font-weight: 400; display: block; line-height: 1.1; }
  .opponent { font-size: 41px; font-weight: 400; color: var(--teal); transform: rotate(-3deg); white-space: nowrap; }

  /* Match screen */
  .status-bar { left: 0; top: 4px; width: 572px; height: 30px; font-size: 19px; color: var(--white); }
  .status-bar .time { position: absolute; left: 0; width: 572px; text-align: center; top: 4px; }
  .status-bar .battery-pct { position: absolute; right: 56px; top: 4px; }
  .score-box {
    top: 108px; width: 72px; height: 60px; background: var(--score-bg); color: var(--green-dark);
    font-size: 44px; font-weight: 600; display: flex; align-items: center; justify-content: center;
    transform: rotate(-3deg); box-shadow: 0 5px 0 #14865c;
  }
  .score-colon { left: 284px; top: 108px; font-size: 40px; color: var(--white); font-weight: 600; }
  .player-name { font-size: 30px; font-weight: 600; color: var(--white); transform: rotate(-3deg); white-space: nowrap; }
  .name-stripes { height: 14px; border-top: 3px solid var(--row-edge); border-bottom: 3px solid var(--row-edge); transform: rotate(-4deg); opacity: 0.7; }
  .rounds-panel { left: 34px; top: 270px; width: 504px; height: 610px; transform: skewY(-3deg); }
  .round-row { position: relative; height: 122px; background: var(--panel); border-bottom: 3px solid var(--panel-line); }
  .round-row:nth-child(odd) { background: #701b93; }
  .round-label { width: 200px; left: 186px; text-align: center; transform: rotate(-3deg); white-space: nowrap; }
  .round-label .title { display: block; font-size: 33px; font-weight: 600; color: var(--teal-soft); }
  .round-label .cat { display: block; font-size: 26px; font-weight: 400; color: var(--lilac); margin-top: 8px; }
  .round-label--open .title { color: var(--lilac); }
  .dots { left: 0; top: 0; width: 572px; height: 1008px; pointer-events: none; }
  .dot-red { fill: var(--red-dot); }
  .dot-green { fill: var(--green-dot); }
  .dot-empty { fill: none; stroke: var(--teal); stroke-width: 2; }
  .bottom-fade { left: 0; top: 860px; width: 572px; height: 148px; background: linear-gradient(180deg, rgba(20, 60, 80, 0) 0%, #133847 100%); }
  .resume-btn {
    left: 120px; top: 890px; width: 330px; height: 72px; background: var(--green-btn); color: var(--green-dark);
    font-size: 40px; font-weight: 600; display: flex; align-items: center; justify-content: center;
    transform: rotate(-3deg); box-shadow: 0 6px 0 #138a5c; white-space: nowrap;
  }
</style>
</head>
<body>

<!-- Games list screen -->
<section class="screen screen--games">
  <div class="avatar" style="left:52px;top:77px;width:138px;height:154px;">
    <svg viewBox="0 0 100 112" role="img" aria-label="Player avatar portrait">
      <polygon points="50,2 97,29 97,83 50,110 3,83 3,29" fill="#2a8f8f"/>
      <polygon points="50,8 92,32 92,80 50,104 8,80 8,32" fill="var(--avatar-fill)"/>
    </svg>
  </div>
  <div class="abs username">Username</div>
  <div class="abs header-band"></div>
  <div class="abs create-btn">Create new Game</div>

  <div class="abs section-label" style="left:46px;top:386px;">My Turn</div>
  <div class="abs game-row" style="top:446px;"></div>
  <div class="avatar" style="left:52px;top:440px;width:96px;height:108px;">
    <svg viewBox="0 0 100 112" role="img" aria-label="Player avatar portrait">
      <polygon points="50,2 97,29 97,83 50,110 3,83 3,29" fill="#2a8f8f"/>
      <polygon points="50,8 92,32 92,80 50,104 8,80 8,32" fill="var(--avatar-fill)"/>
    </svg>
  </div>
  <div class="abs round-info" style="left:226px;top:432px;"><span class="round">Round 2</span><span class="score">3 : 7</span></div>
  <div class="abs opponent" style="left:372px;top:456px;">Opponent</div>

  <div class="abs section-label" style="left:46px;top:590px;">Waiting for Player</div>
  <div class="abs game-row" style="top:650px;"></div>
  <div class="avatar" style="left:52px;top:644px;width:96px;height:108px;">
    <svg viewBox="0 0 100 112" role="img" aria-label="Player avatar portrait">
      <polygon points="50,2 97,29 97,83 50,110 3,83 3,29" fill="#2a8f8f"/>
      <polygon points="50,8 92,32 92,80 50,104 8,80 8,32" fill="var(--avatar-fill)"/>
    </svg>
  </div>
  <div class="abs round-info" style="left:226px;top:636px;"><span class="round">Round 2</span><span class="score">3 : 7</span></div>
  <div class="abs opponent" style="left:372px;top:660px;">Opponent</div>

  <div class="abs section-label section-label--done" style="left:46px;top:796px;">Finished Game</div>
  <div class="abs game-row" style="top:856px;"></div>
  <div class="avatar" style="left:52px;top:852px;width:96px;height:108px;">
    <svg viewBox="0 0 100 112" role="img" aria-label="Player avatar portrait">
      <polygon points="50,2 97,29 97,83 50,110 3,83 3,29" fill="#2a8f8f"/>
      <polygon points="50,8 92,32 92,80 50,104 8,80 8,32" fill="var(--avatar-fill)"/>
    </svg>
  </div>
  <div class="abs round-info" style="left:226px;top:842px;"><span class="round">Round 2</span><span class="score">3 : 7</span></div>
  <div class="abs opponent" style="left:372px;top:866px;">Opponent</div>
</section>

<!-- Match overview screen -->
<section class="screen screen--match">
  <div class="abs status-bar">
    <svg class="abs" style="left:12px;top:10px;" width="60" height="12" viewBox="0 0 60 12">
      <circle cx="6" cy="6" r="5" fill="#fff"/><circle cx="17" cy="6" r="5" fill="#fff"/><circle cx="28" cy="6" r="5" fill="#fff"/>
      <circle cx="39" cy="6" r="4.3" fill="none" stroke="#fff" stroke-width="1.2"/><circle cx="50" cy="6" r="4.3" fill="none" stroke="#fff" stroke-width="1.2"/>
    </svg>
    <svg class="abs" style="left:174px;top:8px;" width="22" height="16" viewBox="0 0 22 16">
      <path d="M2 6 A13 13 0 0 1 20 6" fill="none" stroke="#fff" stroke-width="2"/>
      <path d="M5.5 9.5 A8 8 0 0 1 16.5 9.5" fill="none" stroke="#fff" stroke-width="2"/>
      <circle cx="11" cy="13.5" r="2" fill="#fff"/>
    </svg>
    <span class="time">4:21 PM</span>
    <span class="battery-pct">100%</span>
    <svg class="abs" style="right:10px;top:9px;" width="42" height="16" viewBox="0 0 42 16">
      <rect x="1" y="1" width="36" height="14" rx="2" fill="none" stroke="#fff" stroke-width="1.5"/>
      <rect x="3" y="3" width="32" height="10" rx="1" fill="#fff"/>
      <rect x="38.5" y="5" width="2.5" height="6" fill="#fff"/>
    </svg>
  </div>

  <div class="avatar" style="left:51px;top:61px;width:138px;height:154px;">
    <svg viewBox="0 0 100 112" role="img" aria-label="Player one avatar portrait">
      <polygon points="50,2 97,29 97,83 50,110 3,83 3,29" fill="#2a8f8f"/>
      <polygon points="50,8 92,32 92,80 50,104 8,80 8,32" fill="var(--avatar-fill)"/>
    </svg>
  </div>
  <div class="abs score-box" style="left:190px;">15</div>
  <div class="abs score-colon">:</div>
  <div class="abs score-box" style="left:304px;">12</div>
  <div class="avatar" style="left:377px;top:42px;width:138px;height:154px;">
    <svg viewBox="0 0 100 112" role="img" aria-label="Player two avatar portrait">
      <polygon points="50,2 97,29 97,83 50,110 3,83 3,29" fill="#c0204a"/>
      <polygon points="50,8 92,32 92,80 50,104 8,80 8,32" fill="var(--avatar-fill)"/>
    </svg>
  </div>

  <div class="abs name-stripes" style="left:0;top:254px;width:150px;"></div>
  <div class="abs player-name" style="left:66px;top:232px;">Player 1</div>
  <div class="abs name-stripes" style="left:420px;top:230px;width:152px;"></div>
  <div class="abs player-name" style="left:400px;top:208px;">Player 2</div>

  <div class="abs rounds-panel">
    <div class="round-row"></div>
    <div class="round-row"></div>
    <div class="round-row"></div>
    <div class="round-row"></div>
    <div class="round-row"></div>
  </div>

  <div class="abs round-label" style="top:292px;"><span class="title">Round 1</span><span class="cat">Category</span></div>
  <div class="abs round-label" style="top:406px;"><span class="title">Round 2</span><span class="cat">Category</span></div>
  <div class="abs round-label round-label--open" style="top:520px;"><span class="title">Round 3</span><span class="cat">Category</span></div>
  <div class="abs round-label round-label--open" style="top:634px;"><span class="title">Round 4</span><span class="cat">Category</span></div>
  <div class="abs round-label round-label--open" style="top:748px;"><span class="title">Round 5</span><span class="cat">Category</span></div>

  <svg class="abs dots" viewBox="0 0 572 1008">
    <defs><polygon id="hex" points="0,-14 12.5,-7 12.5,7 0,14 -12.5,7 -12.5,-7"/></defs>
    <use href="#hex" x="96" y="370" class="dot-red"/><use href="#hex" x="138" y="368" class="dot-green"/><use href="#hex" x="180" y="365" class="dot-red"/>
    <use href="#hex" x="389" y="346" class="dot-green"/><use href="#hex" x="431" y="344" class="dot-green"/><use href="#hex" x="473" y="341" class="dot-green"/>
    <use href="#hex" x="96" y="484" class="dot-green"/><use href="#hex" x="138" y="482" class="dot-red"/><use href="#hex" x="180" y="479" class="dot-green"/>
    <use href="#hex" x="389" y="460" class="dot-red"/><use href="#hex" x="431" y="458" class="dot-red"/><use href="#hex" x="473" y="455" class="dot-green"/>
    <use href="#hex" x="96" y="598" class="dot-empty"/><use href="#hex" x="138" y="596" class="dot-empty"/><use href="#hex" x="180" y="593" class="dot-empty"/>
    <use href="#hex" x="389" y="574" class="dot-empty"/><use href="#hex" x="431" y="572" class="dot-empty"/><use href="#hex" x="473" y="569" class="dot-empty"/>
    <use href="#hex" x="96" y="712" class="dot-empty"/><use href="#hex" x="138" y="710" class="dot-empty"/><use href="#hex" x="180" y="707" class="dot-empty"/>
    <use href="#hex" x="389" y="688" class="dot-empty"/><use href="#hex" x="431" y="686" class="dot-empty"/><use href="#hex" x="473" y="683" class="dot-empty"/>
    <use href="#hex" x="96" y="826" class="dot-empty"/><use href="#hex" x="138" y="824" class="dot-empty"/><use href="#hex" x="180" y="821" class="dot-empty"/>
    <use href="#hex" x="389" y="802" class="dot-empty"/><use href="#hex" x="431" y="800" class="dot-empty"/><use href="#hex" x="473" y="797" class="dot-empty"/>
  </svg>

  <div class="abs bottom-fade"></div>
  <div class="abs resume-btn">Resume Game</div>
</section>

</body>
</html>
```